Kitchen and cabinets Landing Page design

Hi there
Web Design Task Outline
• Create a Web Design
• Uncoded webpage layout design
• Single Page - Just Homepage Layout
Task Description
* While we need to update our website, we are actually looking at working with a web designer long-term, which will include quite regular design work. So even though this is a small job, we’d love you to respond, as if you do a good job on this one, we would love to continue working with you on a more regular basis.
Please find below all the information for the design of our new website.
The current Web site is www.brindlecourt.com.au – don’t laugh!!!
Site Basics:
The site will be the landing page and online home of our kitchen renovation business. We also do vanities, bedroom robes and general cabinetery for the house and office.
Target audience:
? Predominantly home renovation seekers, families (females – decision maker) and builders.
? Most of our business comes from referrals and recommendations, but the site needs to be updated to improve our on line image
General feeling to be conveyed:
Update our old, tired 80’s site (fresh, modern and vital)
Must portray contemporary and up to date attitude - eye-catching / attention grabbing
But not too expensive looking as to alienate people who may think we look too expensive
Landing Page:
Happy to look at your creativity, but must contain a capturing image, contact details (phone), testimonials
Potential Nav Links =
Home
Photo Gallery
Contact Us
Testimonial
Vanities
Entertainment Units
Colours:
Our business has little to do with wood now so the timber look is superseded. We are open to your creative suggestions. We need all marketing media to be consistent and the website can start this process. Our logo is really weak and dated as well. At present we have a green and blue business card with capital BC logo (hmmm), but we’re generally thinking something that represents the home and kitchen
Layout: Open to your creativity
* Samples of Other Good (Similar) Sites We Like:
www.hobnookworks.com.au
www.plimo.com.au
www.paramountjoinery.com.au/
www.vellumhomes.com.au
www.thecabinetmanor.com.au
Header Text =
Feel free to submit something from your own creative ideas.
Header Image/photo Ideas:
As the site is about kitchen and house hold cabinets, feel free to use an image to reflect that. We are generally thinking to have one main image that is quite eye-catching and attention grabbing. We can supply photos from jobs we have done later.
* Notes:
1. Do not feel completely bound to these ideas. Feel free to convey the basic idea however your creativity desires.
Thanks a lot and look forward to receiving your first design!
Cheers
Gareth
Updates
sorry people - forgot to mention our best selling point!
we were established in 1980, so have been going for 30 years. This is a strong selling point.
We use "30 years of excellence" as a tag.
there are numerous ways of using est. 1980, ie gold label, starburst etc. Go for it.
thanks
Gareth
Hi Designers, My apologies for the delay in responding to your designs. I have been working on other business and have not had a chance to look at them thoroughly. I plan to focus on them today and will provide feedback. Thank you for your understanding.
Reason: Today was the first chance I've had to look at designs. Will be actively providing feedback over next fews day. Am looking to make some changes to the a few of the designs received. Thanks everyone for you patience.

```html
<!DOCTYPE html>
<html lang="en">
<head>
<meta charset="utf-8">
<title>Brindle Court – Cabinets &amp; Furniture</title>
<link rel="stylesheet" href="https://fonts.googleapis.com/css2?family=Questrial&family=Arimo:wght@400;700&display=swap">
<style>
:root{
  --wood-dark:#3e1d0c;
  --wood-mid:#7a3f1c;
  --wood-light:#b06a35;
  --frame:rgba(150,90,55,.55);
  --panel:#f6f3ef;
  --panel-edge:#d7d3cf;
  --ink:#1b1b1b;
  --tan:#c9935b;
  --tan-dark:#a7713d;
  --kitchen-light:#ece6dc;
  --kitchen-mid:#c9bfb1;
  --floor:#8a3a22;
  --dark:#050505;
  --white:#fff;
}
*{box-sizing:border-box;margin:0;padding:0}
html,body{width:1200px;height:846px;overflow:hidden}
body{
  position:relative;
  font-family:"Arimo",Arial,sans-serif;
  color:var(--ink);
  background:linear-gradient(90deg,var(--wood-dark) 0%,var(--wood-mid) 22%,var(--wood-light) 50%,var(--wood-mid) 78%,var(--wood-dark) 100%);
}
.abs{position:absolute}
.frame{left:131px;top:21px;width:936px;height:793px;border-radius:14px;background:var(--frame)}
.page{left:150px;top:37px;width:898px;height:762px;border-radius:12px;background:linear-gradient(#f3efeb,#fbfaf8 30%,#fdfcfb);box-shadow:0 1px 4px rgba(0,0,0,.4)}
.brand{left:171px;top:45px;width:182px;height:122px;display:flex;align-items:center;gap:8px;font-family:"Questrial",sans-serif;font-size:25px;color:var(--tan-dark)}
.brand-dot{width:14px;height:14px;border-radius:50%;background:var(--tan-dark);flex:none}
.search{left:838px;top:60px;width:181px;height:20px;border:1px solid #b9b5b1;border-radius:10px;background:var(--white);font-family:"Questrial",sans-serif;font-size:11px;color:#555;padding:3px 0 0 12px}
.search-btn{position:absolute;right:0;top:0;width:26px;height:18px;border-left:1px solid #b9b5b1}
.contact{right:173px;top:97px;font-family:"Questrial",sans-serif;font-size:17px;color:var(--ink);white-space:nowrap}
.nav{left:470px;top:127px;width:562px;height:31px;border:1px solid #d3cfcb;border-radius:7px;background:var(--white);display:flex;align-items:center;font-family:"Questrial",sans-serif;font-size:13.5px;overflow:hidden}
.nav a{color:var(--ink);text-decoration:none;padding:0 10px}
.nav .sep{color:#333}
.nav .active{background:linear-gradient(#dba56d,var(--tan-dark));color:var(--white);height:100%;display:flex;align-items:center;padding:0 11px;font-size:15px;border-radius:6px 0 0 6px;margin-right:1px}
.hero{left:168px;top:181px;width:864px;height:414px;border-radius:8px;overflow:hidden;border:1px solid var(--panel-edge);
  background:linear-gradient(180deg,var(--kitchen-light) 0%,#e3ddd2 55%,var(--kitchen-mid) 75%,var(--floor) 100%)}
.thumbs{left:169px;top:212px;width:125px;height:332px;border-radius:8px;background:var(--dark)}
.thumb{position:absolute;left:12px;width:99px;height:79px;border-radius:7px;border:1px solid #777}
.thumb.t1{top:33px;background:linear-gradient(#c6bfb5,#8b3c20)}
.thumb.t2{top:124px;background:linear-gradient(#d8d3cc,#6b5642)}
.thumb.t3{top:215px;background:linear-gradient(#e4e1dc,#5a3a26)}
.round-btn{position:absolute;left:50px;width:25px;height:25px;border-radius:50%;background:#555}
.tab{left:281px;top:342px;width:31px;height:55px}
.hero-note{left:715px;top:451px;width:316px;height:114px;border-radius:8px;background:rgba(255,255,255,.82);padding:6px 12px;font-size:12.6px;line-height:16.6px}
.hero-note .more{display:block;margin-top:2px}
.mission{left:176px;top:581px;width:848px;height:31px;border-radius:8px;background:linear-gradient(#d9a36c,var(--tan-dark));color:var(--white);font-weight:700;font-size:13.4px;padding:7px 0 0 28px;text-shadow:0 1px 1px rgba(0,0,0,.45);white-space:nowrap;overflow:hidden}
.card{top:637px;height:139px;border:1px solid var(--panel-edge);border-radius:12px;background:linear-gradient(#fcfbfa,#eeece9)}
.c1{left:168px;width:292px}
.c2{left:475px;width:250px}
.c3{left:740px;width:292px}
.mini{position:absolute;left:12px;width:88px;height:56px;border:2px solid var(--white);border-radius:6px;box-shadow:0 0 2px rgba(0,0,0,.5)}
.mini.m1{top:10px;background:linear-gradient(#c6bfb5,#8b3c20)}
.mini.m2{top:73px;background:linear-gradient(#e4e1dc,#5a3a26)}
.mini-text{position:absolute;left:106px;width:180px;font-size:10.4px;line-height:13.5px}
.gallery-img{position:absolute;left:16px;top:7px;width:218px;height:101px;border:2px solid var(--white);border-radius:6px;box-shadow:0 0 2px rgba(0,0,0,.5);background:linear-gradient(#d9d3c9,#f1eee9 60%,#cfc6ba)}
.gallery-cap{position:absolute;left:0;right:0;top:114px;text-align:center;font-family:"Questrial",sans-serif;font-size:14.5px}
.side-arrow{top:690px;width:25px;height:25px}
.news-title{position:absolute;left:14px;top:8px;font-family:"Questrial",sans-serif;font-size:16px}
.rss{position:absolute;left:247px;top:6px;width:26px;height:26px;border-radius:5px;background:linear-gradient(#f9b25a,#ec7a1a)}
.news-text{position:absolute;left:15px;top:33px;width:270px;font-size:10.4px;line-height:13.5px}
.field{position:absolute;left:11px;width:181px;height:20px;border:1px solid #b9b5b1;border-radius:10px;background:var(--white);font-size:9.5px;padding:4px 0 0 8px}
.submit{position:absolute;left:197px;top:103px;width:78px;height:21px;border-radius:10px;background:linear-gradient(#dba56d,var(--tan-dark));color:var(--white);font-weight:700;font-size:13px;text-align:center;padding-top:2px;text-shadow:0 1px 1px rgba(0,0,0,.4)}
.copyright{left:0;width:1200px;top:821px;text-align:center;font-size:10.5px;color:var(--white)}
</style>
</head>
<body>
<div class="abs frame" role="img" aria-label="Timber grain backdrop"></div>
<div class="abs page"></div>

<header>
  <div class="abs brand"><span class="brand-dot"></span>Brindle Court</div>
  <div class="abs search">Search...
    <span class="search-btn"><svg width="26" height="18" viewBox="0 0 26 18"><circle cx="12" cy="8" r="4.5" fill="none" stroke="#777" stroke-width="1.5"/><line x1="15.3" y1="11.3" x2="18.5" y2="14.5" stroke="#777" stroke-width="1.8"/></svg></span>
  </div>
  <div class="abs contact">Tel: 03 9418-2260 &nbsp;|&nbsp; Fax: 03 9418-2261</div>
  <nav class="abs nav">
    <a class="active" href="#">Home</a>
    <a href="#">Photo Gallery</a><span class="sep">|</span>
    <a href="#">Contact Us</a><span class="sep">|</span>
    <a href="#">Testimonial</a><span class="sep">|</span>
    <a href="#">Vanities</a><span class="sep">|</span>
    <a href="#">Entertainment Units</a>
  </nav>
</header>

<main>
  <div class="abs hero" role="img" aria-label="Photo of a bright white kitchen with an island bench and timber floor"></div>

  <div class="abs thumbs">
    <span class="round-btn" style="top:4px"><svg width="25" height="25"><path d="M8 15l4.5-4.5L17 15" fill="none" stroke="#fff" stroke-width="2.4"/></svg></span>
    <div class="thumb t1" role="img" aria-label="Kitchen with timber floor"></div>
    <div class="thumb t2" role="img" aria-label="Entertainment unit"></div>
    <div class="thumb t3" role="img" aria-label="Kitchen island"></div>
    <span class="round-btn" style="top:302px"><svg width="25" height="25"><path d="M8 10l4.5 4.5L17 10" fill="none" stroke="#fff" stroke-width="2.4"/></svg></span>
  </div>
  <svg class="abs tab" viewBox="0 0 31 55"><path d="M0 0h6a25 27.5 0 0 1 0 55H0z" fill="#050505"/><path d="M20 19l-8 8.5 8 8.5" fill="none" stroke="#fff" stroke-width="4"/></svg>

  <div class="abs hero-note">We cater for those who truly care about quality, workmanship and a high level of personal service. We are proud of our innovative designs, superior products, and outstanding service sought after by the discerning customers.
    <span class="more">Read More</span></div>

  <div class="abs mission">OUR MISSION: To produce excellent quality cabinetry every time! &nbsp;We cater for those who truly care about quality, workmanship</div>

  <section class="abs card c1">
    <div class="mini m1" role="img" aria-label="Kitchen project"></div>
    <p class="mini-text" style="top:21px">We cater for those who truly care about quality, workmanship and a high level of personal service</p>
    <div class="mini m2" role="img" aria-label="Kitchen project"></div>
    <p class="mini-text" style="top:84px">We cater for those who truly care about quality, workmanship and a high level of personal service</p>
  </section>

  <svg class="abs side-arrow" style="left:463px" viewBox="0 0 25 25"><circle cx="12.5" cy="12.5" r="12.5" fill="#333"/><path d="M14.5 8l-4.5 4.5 4.5 4.5" fill="none" stroke="#fff" stroke-width="2.4"/></svg>
  <section class="abs card c2">
    <div class="gallery-img" role="img" aria-label="Photo of a finished kitchen"></div>
    <p class="gallery-cap">View Our Picture Gallery</p>
  </section>
  <svg class="abs side-arrow" style="left:711px" viewBox="0 0 25 25"><circle cx="12.5" cy="12.5" r="12.5" fill="#333"/><path d="M10.5 8l4.5 4.5-4.5 4.5" fill="none" stroke="#fff" stroke-width="2.4"/></svg>

  <section class="abs card c3">
    <h2 class="news-title">Newsletter</h2>
    <svg class="rss" viewBox="0 0 26 26"><circle cx="7" cy="19" r="2.4" fill="#fff"/><path d="M5 12a9 9 0 0 1 9 9M5 6a15 15 0 0 1 15 15" fill="none" stroke="#fff" stroke-width="2.6"/></svg>
    <p class="news-text">We cater for those who truly care about quality, workmanship and ahigh level of personal service</p>
    <div class="field" style="top:72px">Name:</div>
    <div class="field" style="top:103px">Email:</div>
    <div class="submit">Submit</div>
  </section>
</main>

<footer class="abs copyright">Copyright © 2011 Brindlecourt.</footer>
</body>
</html>
```